Application for baby milk and water counter

We are building baby food app. Need to design main screen for tha app first so we can go forward to other secondary screens of the app

Food dashboard screen
Food dashboard screen is main page for view/edit food data

General vision
I see the app in pastel colors with some illustrations to make the app more in positive. You can influence from game Lantern Hollow. I see with smooth colors and gradients like in a game. Also need to have animations/transitions for each action. Each click should create smooth transition to new state. My idea is to build one dashboard screen for food which we can reuse it for other screens. So a lot of thinking should go into design stage to app appealing.

Food Dashboard
Current screen should show all the data about food intake of the baby. So here user should see

Milk How much food baby had in ml/oz. So there should be some kind of illustrated bottle or glass or smth that shows it is filled with that amount.

Add/Remove controls for food. Should be some kind of custom control for inputing amount to remove/add. I see it as a slider on the side of the bottle. User slides up or down and amount is added/removed.

Notification. So user should be aware how many hours/minutes left for next food intake. This is optional field, so consider it could be disabled. So no empty space should be on a screen. There should be human readable text. Something like. 1:30 minutes left for next intake. Maybe could be some custom made icons to illustrate that it is next food intake.

Burped: User should have ability to how much baby burped. This amount is integer value. So it could be “Baby burped 2 times today”. So again here I see some custom made/icon to illustrate how many times baby burped and amount next to it. I see changing the value just by tapping, but I don’t know how to edit if user tapped accidentally more than it should be. So TBD here.

Date and time: Dashboard should show for which date it is viewing/editing data. Should be able to change it, so user can add/edit data for yesterday. Don’t want to see here calendar on a screen so need to come up with nice design decision.

Water: User should have ability to view/edit water intake of the baby, but water is secondary information so it should be smaller than milk, or come up with some other idea how to show the water. I see to have same controls for water like for milk. Water intake is optional it can be disabled by the user.

Target Market(s)

For just became mothers

Font styles to use
Sans Serif

Colors
0094D4
00A9DD
6FCCEA
C7EBF8
E9F6FB
FFC000
F8CF3A
FAE287
FDF2CF
FEFAEE
E54698
E96AAD
F1A4CE
F9D9EA
FCEFF6

Requirements
Must have
• Ilustrations or playfull icons for show information

```html
<!DOCTYPE html>
<html lang="en">
<head>
<meta charset="utf-8">
<title>Food Dashboard</title>
<link rel="stylesheet" href="https://fonts.googleapis.com/css2?family=Lato:wght@400;700;900&display=swap">
<style>
:root{
  --blue-deep:#0094D4;
  --blue:#00A9DD;
  --blue-soft:#6FCCEA;
  --blue-pale:#C7EBF8;
  --blue-mist:#E9F6FB;
  --pink:#E54698;
  --pink-mid:#E96AAD;
  --pink-soft:#F1A4CE;
  --pink-pale:#F9D9EA;
  --lavender:#E6E6F3;
  --ink:#2b2b2b;
  --ink-soft:#4a4a4a;
  --label:#7a7a7a;
  --line:#d9d9d9;
  --white:#ffffff;
}
*{box-sizing:border-box;margin:0;padding:0}
html,body{width:675px;height:1200px;overflow:hidden}
body{font-family:'Lato',sans-serif;color:var(--ink);background:var(--white)}
.screen{position:relative;width:675px;height:1200px;overflow:hidden;
  background:linear-gradient(180deg,#fbfbfe 0%,#f7f8fc 100%)}
.sky{position:absolute;left:0;top:0;width:675px;height:440px}
.hero-art{position:absolute;left:200px;top:0;width:275px;height:240px;border-radius:40% 40% 45% 45%;
  background:radial-gradient(circle at 45% 40%,#f6d2b8 0%,#e6cfe8 55%,rgba(230,230,243,0) 75%)}
.field{position:absolute;top:272px;height:54px;border-bottom:2px dashed #9a9a9a}
.field-date{left:86px;width:193px}
.field-time{left:428px;width:157px}
.field-label{position:absolute;left:4px;top:6px;font-size:25px;color:var(--label)}
.field-icon{position:absolute;right:0;top:6px;width:30px;height:30px}
.card{position:absolute;left:90px;top:356px;width:495px;height:594px;background:var(--white);
  border-radius:6px;box-shadow:0 4px 18px rgba(90,90,140,.14)}
.section{position:absolute;left:0;width:495px}
.section+.section{border-top:2px solid var(--line)}
.section-title{position:absolute;left:54px;font-size:25px;font-weight:900;color:var(--blue-deep)}
.section-art{position:absolute;left:54px;border-radius:14px}
.stat{position:absolute}
.stat-label{font-size:28px;font-weight:900;color:var(--ink)}
.stat-value{font-size:20px;color:var(--ink-soft);margin-top:16px}
.stepper{position:absolute;display:flex;gap:20px}
.step{width:25px;height:25px;border-radius:50%;display:block}
.toggle{position:absolute;width:46px;height:24px;border-radius:12px;background:var(--blue-deep)}
.toggle::after{content:"";position:absolute;right:3px;top:3px;width:18px;height:18px;border-radius:50%;background:var(--white)}
.corner-art{position:absolute;left:0;top:880px;width:220px;height:320px;
  background:linear-gradient(160deg,rgba(199,235,248,.9) 0%,rgba(233,246,251,.7) 55%,rgba(249,217,234,.6) 100%);
  border-radius:0 90px 0 0}
.reminder{position:absolute;left:94px;top:999px;width:487px;height:65px;border-radius:4px;background:var(--pink);
  display:flex;align-items:center;padding:0 0 0 36px;color:var(--white);font-size:19px;font-weight:700}
.reminder .toggle{right:38px;top:20px;background:transparent;border:2px solid var(--white)}
.reminder .toggle::after{top:2px;right:2px;width:16px;height:16px}
</style>
</head>
<body>
<main class="screen">
  <svg class="sky" viewBox="0 0 675 440" aria-hidden="true">
    <defs>
      <linearGradient id="pinkArc" x1="0" y1="0" x2="1" y2="0"><stop offset="0" stop-color="#F9D9EA"/><stop offset="1" stop-color="#FCEFF6"/></linearGradient>
      <linearGradient id="blueArc" x1="0" y1="0" x2="1" y2="0"><stop offset="0" stop-color="#E9F6FB"/><stop offset="1" stop-color="#C7EBF8"/></linearGradient>
    </defs>
    <rect width="675" height="440" fill="#fbfbfe"/>
    <circle cx="180" cy="640" r="440" fill="url(#pinkArc)" opacity=".8"/>
    <circle cx="500" cy="640" r="440" fill="url(#blueArc)" opacity=".8"/>
    <path d="M0 0H675V380Q590 340 500 330Q400 330 337 400Q270 330 170 330Q80 335 0 380Z" fill="var(--lavender)"/>
  </svg>

  <div class="hero-art" role="img" aria-label="Illustration of a smiling baby in a diaper reaching toward a milk bottle"></div>

  <div class="field field-date">
    <span class="field-label">Date</span>
    <svg class="field-icon" viewBox="0 0 24 24" aria-hidden="true"><rect x="3" y="5" width="18" height="16" rx="2" fill="#5c5c5c"/><rect x="3" y="5" width="18" height="4" fill="#3f3f3f"/><rect x="7" y="2" width="2" height="5" fill="#3f3f3f"/><rect x="15" y="2" width="2" height="5" fill="#3f3f3f"/><g fill="#fff"><rect x="6" y="11" width="3" height="3"/><rect x="10.5" y="11" width="3" height="3"/><rect x="15" y="11" width="3" height="3"/><rect x="6" y="15.5" width="3" height="3"/><rect x="10.5" y="15.5" width="3" height="3"/><rect x="15" y="15.5" width="3" height="3"/></g></svg>
  </div>
  <div class="field field-time">
    <span class="field-label">Time</span>
    <svg class="field-icon" viewBox="0 0 24 24" aria-hidden="true"><circle cx="12" cy="12" r="10" fill="#5c5c5c"/><path d="M12 6v6l4 3" stroke="#fff" stroke-width="2" fill="none" stroke-linecap="round"/></svg>
  </div>

  <section class="card">
    <div class="section" style="top:0;height:202px">
      <h2 class="section-title" style="top:42px">Milk</h2>
      <div class="section-art" role="img" aria-label="Illustrated milk bottle" style="top:94px;width:45px;height:81px;background:linear-gradient(180deg,#6FCCEA 0%,#a9e0d8 40%,#6fc7b8 100%)"></div>
      <div class="stat" style="left:157px;top:100px"><div class="stat-label">Total</div><div class="stat-value">200 ml</div></div>
      <div class="stat" style="left:290px;top:100px"><div class="stat-label">In take</div><div class="stat-value">80 ml</div></div>
      <div class="stepper" style="left:373px;top:148px">
        <svg class="step" viewBox="0 0 24 24" aria-label="Add"><circle cx="12" cy="12" r="12" fill="#3d5fb0"/><path d="M12 6v12M6 12h12" stroke="#fff" stroke-width="3"/></svg>
        <svg class="step" viewBox="0 0 24 24" aria-label="Remove"><circle cx="12" cy="12" r="12" fill="var(--pink-mid)"/><path d="M6 12h12" stroke="#fff" stroke-width="3"/></svg>
      </div>
    </div>

    <div class="section" style="top:202px;height:196px">
      <h2 class="section-title" style="top:34px">Water</h2>
      <span class="toggle" style="left:400px;top:37px"></span>
      <div class="section-art" role="img" aria-label="Illustrated water bottle" style="top:88px;width:40px;height:82px;background:linear-gradient(180deg,#F9D9EA 0%,#C7EBF8 35%,#6FCCEA 100%)"></div>
      <div class="stat" style="left:157px;top:90px"><div class="stat-label">Total</div><div class="stat-value">200 ml</div></div>
      <div class="stat" style="left:290px;top:90px"><div class="stat-label">In take</div><div class="stat-value">80 ml</div></div>
      <div class="stepper" style="left:373px;top:138px">
        <svg class="step" viewBox="0 0 24 24" aria-label="Add"><circle cx="12" cy="12" r="12" fill="#3d5fb0"/><path d="M12 6v12M6 12h12" stroke="#fff" stroke-width="3"/></svg>
        <svg class="step" viewBox="0 0 24 24" aria-label="Remove"><circle cx="12" cy="12" r="12" fill="var(--pink-mid)"/><path d="M6 12h12" stroke="#fff" stroke-width="3"/></svg>
      </div>
    </div>

    <div class="section" style="top:398px;height:196px">
      <h2 class="section-title" style="top:34px">Burped</h2>
      <div class="section-art" role="img" aria-label="Illustration of a sitting baby" style="top:80px;width:64px;height:72px;background:radial-gradient(circle at 50% 35%,#f8cf9a 0%,#e9eef6 65%,#ffffff 100%)"></div>
      <div class="stat" style="left:157px;top:92px"><div class="stat-label">Total</div><div class="stat-value">2 Times</div></div>
      <div class="stepper" style="left:302px;top:140px">
        <svg class="step" viewBox="0 0 24 24" aria-label="Add"><circle cx="12" cy="12" r="12" fill="#3d5fb0"/><path d="M12 6v12M6 12h12" stroke="#fff" stroke-width="3"/></svg>
        <svg class="step" viewBox="0 0 24 24" aria-label="Remove"><circle cx="12" cy="12" r="12" fill="var(--pink-mid)"/><path d="M6 12h12" stroke="#fff" stroke-width="3"/></svg>
      </div>
    </div>
  </section>

  <div class="corner-art" role="img" aria-label="Illustration of a baby hugging a large milk bottle"></div>

  <div class="reminder">
    <span>2 Hours 40 Minutes left for next intake</span>
    <span class="toggle"></span>
  </div>
</main>
</body>
</html>
```